New Business Card Design Project

We are looking for a talented individual to create a truly awesome/unique business card design for us. We are looking for a someone to design something that will really stand out from the crowd - we don't mind what ideas you come up with (ie embossed/flat/matte/shine etc etc) just wow us with your creativity.
Updates

Target Market(s)

Video Games Industry Professionals (all levels of seniority from QA Testers through to CEOs)

Contact Information for Business Card

Company logo (see upload)
Company name: Northbay Play Careers Ltd
Employee Name: Darren Elsby
Job title: CEO
Website: www.nbpc2go.example
Office +44 1632 960418
Mobile: +44 7700 900276
Email: darren@nbpc2go.example

Colors

Designer to choose colors to be used in the design.

Requirements
Must have
• The business card design MUST contain all the information listed in the BUSINESS CARD DETAILS box.
• You will see the colours that are relevant to us (ie company logo) in the uploaded imagery - however you do not have to use all these colours when designing the business card itself
• MUST BE DOUBLE SIDED

```html
<!DOCTYPE html>
<html lang="en">
<head>
<meta charset="utf-8">
<title>Northbay Play Careers – Business Card</title>
<link rel="stylesheet" href="https://fonts.googleapis.com/css2?family=Exo+2:wght@600;700&family=Questrial&display=swap">
<style>
  :root {
    --navy: #061641;
    --navy-text: #0c1a8a;
    --orange: #f26a10;
    --orange-soft: #f7a23a;
    --white: #ffffff;
    --ink: #111111;
    --bg-warm: #fbd9b8;
    --bg-light: #f6f1c4;
    --shadow: rgba(40, 20, 0, 0.35);
  }
  * { margin: 0; padding: 0; box-sizing: border-box; }
  html, body { width: 1200px; height: 1200px; overflow: hidden; }
  body {
    position: relative;
    background: radial-gradient(circle at 40% 60%, var(--bg-light) 0%, var(--bg-warm) 100%);
    font-family: "Questrial", "Century Gothic", sans-serif;
  }
  .card {
    position: absolute;
    overflow: hidden;
    box-shadow: 0 14px 30px var(--shadow);
  }
  .card-front {
    left: 103px; top: 86px; width: 873px; height: 497px;
    background: var(--navy);
  }
  .card-back {
    left: 221px; top: 623px; width: 869px; height: 496px;
    background: var(--navy);
  }
  .brand-mark {
    position: absolute;
    border-radius: 50%;
    background: radial-gradient(circle at 40% 35%, var(--orange-soft), var(--orange));
  }
  .card-front .brand-mark { left: 245px; top: 52px; width: 280px; height: 280px; }
  .card-back .brand-mark { left: 51px; top: 87px; width: 290px; height: 290px; }

  .brand-name {
    position: absolute;
    font-family: "Exo 2", sans-serif;
    font-weight: 700;
    text-align: center;
    line-height: 1;
  }
  .card-front .brand-name {
    left: 0; width: 938px; top: 366px;
    color: var(--white);
    font-size: 58px;
  }
  .card-front .brand-name span { display: block; }
  .card-front .brand-name .line-2 { font-size: 42px; margin-top: 12px; }

  .info-panel {
    position: absolute; inset: 0;
    width: 100%; height: 100%;
  }
  .card-back .brand-name {
    left: 460px; width: 390px; top: 38px;
    color: var(--navy-text);
    font-size: 44px;
  }
  .card-back .brand-name span { display: block; }
  .card-back .brand-name .line-2 { margin-top: 4px; }

  .website {
    position: absolute;
    left: 460px; width: 390px; top: 152px;
    text-align: center;
    font-size: 21px;
    color: var(--ink);
  }
  .person-name {
    position: absolute;
    left: 491px; top: 218px;
    font-family: "Exo 2", sans-serif;
    font-weight: 700;
    font-size: 34px;
    color: var(--navy-text);
  }
  .job-title {
    position: absolute;
    left: 493px; top: 266px;
    font-family: "Exo 2", sans-serif;
    font-weight: 600;
    font-size: 21px;
    color: var(--ink);
  }
  .contact-list { list-style: none; }
  .contact-item {
    position: absolute;
    left: 486px;
    display: flex; align-items: center;
    font-size: 21px;
    color: var(--ink);
  }
  .contact-item svg { width: 34px; height: 34px; margin-right: 13px; fill: var(--ink); }
  .contact-office { top: 318px; }
  .contact-mobile { top: 370px; }
  .contact-email { top: 415px; }
</style>
</head>
<body>

<section class="card card-front" aria-label="Business card front">
  <div class="brand-mark" aria-hidden="true"></div>
  <h1 class="brand-name"><span class="line-1">Northbay Play</span><span class="line-2">Careers</span></h1>
</section>

<section class="card card-back" aria-label="Business card back">
  <div class="brand-mark" aria-hidden="true"></div>
  <svg class="info-panel" viewBox="0 0 869 496" preserveAspectRatio="none" aria-hidden="true">
    <polygon points="416,0 869,0 869,496 451,496" fill="#ffffff"/>
  </svg>
  <h2 class="brand-name"><span class="line-1">Northbay Play</span><span class="line-2">Careers</span></h2>
  <p class="website">www.nbpc2go.example</p>
  <p class="person-name">Darren Elsby</p>
  <p class="job-title">CEO</p>
  <ul class="contact-list">
    <li class="contact-item contact-office">
      <svg viewBox="0 0 24 24" aria-hidden="true"><path d="M6.6 10.8c1.4 2.8 3.8 5.1 6.6 6.6l2.2-2.2c.3-.3.7-.4 1-.2 1.1.4 2.3.6 3.6.6.6 0 1 .4 1 1V20c0 .6-.4 1-1 1C10.6 21 3 13.4 3 4c0-.6.4-1 1-1h3.5c.6 0 1 .4 1 1 0 1.3.2 2.5.6 3.6.1.3 0 .7-.2 1l-2.3 2.2z"/></svg>
      <span>+44 1632 960418</span>
    </li>
    <li class="contact-item contact-mobile">
      <svg viewBox="0 0 24 24" aria-hidden="true"><path d="M8 1h8a2 2 0 0 1 2 2v18a2 2 0 0 1-2 2H8a2 2 0 0 1-2-2V3a2 2 0 0 1 2-2zm0 3v15h8V4H8zm4 16.2a.9.9 0 1 0 0 1.8.9.9 0 0 0 0-1.8z"/></svg>
      <span>+44 7700 900276</span>
    </li>
    <li class="contact-item contact-email">
      <svg viewBox="0 0 24 24" aria-hidden="true"><path d="M2 5h20v14H2V5zm2 2v.2l8 5.5 8-5.5V7H4zm16 2.6-8 5.5-8-5.5V17h16V9.6z"/></svg>
      <span>darren@nbpc2go.example</span>
    </li>
  </ul>
</section>

</body>
</html>
```